Bright Path Mentors Needs A New Website Design

We need a 8 page website designed for "Bright Path Mentors .ca" similar in design to: "keystone learning hub .com".

The winner/successful candidate on the home page will be asked to complete the following inner pages to complete the project:

About Us
Philosophy
How We Work
Work With Us
Blog
Find A Tutor
Contact

Target Market(s)

Tutoring business clients/children

Industry/Entity Type

Education

Number of Pages Required

5+ page

Font styles to use
Sans Serif

Requirements
Must have
• The attached logo included of course. Similar design to the design provided above in the brief. Clear high quality high resolution images of children in school settings.

```html
<!DOCTYPE html>
<html lang="en">
<head>
<meta charset="utf-8">
<title>Bright Path Mentors — Home Tutoring</title>
<link rel="stylesheet" href="https://fonts.googleapis.com/css2?family=Lato:ital,wght@0,300;0,400;0,700;0,900;1,400&display=swap">
<style>
:root{
  --blue:#2c3e9e;
  --blue-dark:#233285;
  --orange:#f26a16;
  --red:#e85547;
  --yellow:#f8b422;
  --cream:#fdf4e3;
  --grey-band:#ececec;
  --dark:#2a2a2a;
  --text:#444;
  --muted:#888;
  --white:#fff;
}
*{margin:0;padding:0;box-sizing:border-box}
html,body{width:1200px;height:5143px;overflow:hidden}
body{font-family:"Lato",sans-serif;color:var(--text);background:var(--white);position:relative}
.abs{position:absolute}
p{line-height:1.6}

/* header */
.site-header{position:absolute;top:0;left:0;width:1200px;height:137px;background:var(--blue)}
.brand{position:absolute;left:150px;top:0;width:210px;height:200px;background:var(--white);border:6px solid var(--blue);display:flex;flex-direction:column;align-items:center;justify-content:center;gap:12px;z-index:3}
.brand-dot{width:54px;height:54px;border-radius:50%;background:var(--orange)}
.brand-name{font-weight:900;font-size:24px;color:var(--blue);text-align:center;line-height:1.1}
.topbar{position:absolute;right:88px;top:10px;display:flex;align-items:center;gap:18px}
.phone{color:var(--white);font-size:15px;display:flex;align-items:center;gap:8px}
.phone-icon{width:26px;height:26px;border-radius:50%;background:var(--orange);display:flex;align-items:center;justify-content:center}
.search{display:flex}
.search span{background:var(--white);width:190px;height:30px;font-size:13px;color:var(--muted);padding:7px 10px}
.search b{background:var(--blue-dark);color:var(--white);font-size:13px;padding:7px 12px;border:1px solid var(--white)}
.main-nav{position:absolute;left:380px;top:82px;display:flex;gap:34px}
.main-nav a{color:var(--white);text-decoration:none;font-size:15px;font-weight:700;letter-spacing:.3px;padding-bottom:8px}
.main-nav a.active{border-bottom:3px solid var(--orange)}

/* hero */
.hero{position:absolute;top:137px;left:0;width:1200px;height:693px;background:linear-gradient(100deg,#c98a6c 0%,#b96d5a 25%,#8c7a72 55%,#d8d4cf 100%)}
.hero-copy{position:absolute;top:235px;width:100%;text-align:center;color:var(--white)}
.hero-kicker{font-size:30px;font-weight:300;letter-spacing:6px;display:flex;justify-content:center;align-items:center;gap:18px}
.hero-kicker::before,.hero-kicker::after{content:"";width:90px;height:1px;background:var(--white)}
.hero-title{font-size:72px;font-weight:700;letter-spacing:2px;margin-top:6px}
.hero-rule{width:90px;height:3px;background:var(--white);margin:14px auto}
.hero-sub{font-size:26px;font-style:italic}

/* intro */
.intro-title{left:89px;top:895px;font-size:31px;font-weight:900;color:var(--orange)}
.intro-lead{left:89px;top:940px;width:520px;font-size:19px;font-style:italic;color:#333;line-height:1.3}
.intro-body{left:89px;top:1010px;width:520px;font-size:13px;line-height:1.55}
.ticks{left:89px;top:1158px;list-style:none;font-size:13px}
.ticks li{margin-bottom:8px;display:flex;gap:10px;align-items:center}
.ticks li::before{content:"";width:10px;height:10px;background:#333}
.intro-photo{left:645px;top:943px;width:460px;height:308px;background:linear-gradient(135deg,#4d7a4a,#9a7a5e 55%,#c6ab90)}
.quote-box{left:89px;top:1296px;width:1022px;height:140px;background:var(--red);color:var(--white);text-align:center;padding:26px 120px}
.quote-box p{font-size:19px;line-height:1.45}
.quote-box .who{font-size:14px;font-weight:700;margin-top:12px}
.quote-mark{position:absolute;left:30px;top:16px;font-size:70px;font-weight:900;color:#f08a7e;line-height:1}

/* hexagons */
.hex-band{top:1485px;left:0;width:1200px;height:395px;background:var(--grey-band)}
.hex{position:absolute;top:58px;width:310px;height:292px}
.hex svg{position:absolute;inset:0}
.hex-text{position:absolute;top:92px;width:100%;text-align:center;color:var(--white);font-size:24px;line-height:1.2}
.hex-btn{position:absolute;top:205px;left:50%;transform:translateX(-50%);background:var(--white);color:var(--orange);font-size:13px;font-weight:700;padding:8px 20px;white-space:nowrap}

/* video */
.video-title{left:89px;top:1940px;width:480px;font-size:30px;font-weight:900;color:var(--orange);line-height:1.1}
.video-body{left:89px;top:2015px;width:480px;font-size:13px}
.btn-orange{background:var(--orange);color:var(--white);font-size:13px;font-weight:700;padding:9px 18px}
.badge{left:600px;top:1955px;width:70px;height:70px;border-radius:50%;background:radial-gradient(#f6d266,#c99a1d);border:4px solid #e8c04a}
.video{left:727px;top:1955px;width:377px;height:240px;background:linear-gradient(160deg,#f2efe8,#d8cfc0)}
.play{position:absolute;left:158px;top:90px;width:62px;height:62px;border-radius:50%;background:rgba(0,0,0,.6)}

/* why */
.why{top:2264px;left:0;width:1200px;height:669px;background:var(--yellow)}
.why h2{position:absolute;top:42px;width:100%;text-align:center;color:var(--white);font-size:34px;font-weight:900}
.why h2::after{content:"";display:block;width:70px;height:3px;background:var(--white);margin:10px auto 0}
.feature{position:absolute;width:494px;height:146px;background:var(--white);padding:20px 20px 0 110px}
.feature-icon{position:absolute;left:18px;top:20px;width:74px;height:74px;background:var(--cream);display:flex;align-items:center;justify-content:center}
.feature h3{font-size:16px;font-weight:700;color:#222;margin-bottom:6px}
.feature p{font-size:12px;line-height:1.45;color:var(--muted)}

/* testimonial */
.testi{top:2933px;left:0;width:1200px;height:617px;background:linear-gradient(180deg,#3b3b3b,#262626)}
.testi-frame{position:absolute;left:92px;top:96px;width:1016px;height:282px;border:2px solid #8a8a8a;padding:60px 80px;text-align:center;color:#eee;font-size:16px;line-height:1.6}
.avatar{position:absolute;left:570px;top:380px;width:60px;height:60px;border-radius:50%;background:#7f8f9a;border:3px solid var(--white)}
.testi-name{position:absolute;top:455px;width:100%;text-align:center;color:var(--white);font-size:15px}
.arrows{position:absolute;top:508px;left:568px;display:flex;gap:26px}

/* stats */
.stats{top:3550px;left:0;width:1200px;height:326px;background:var(--red);display:flex;justify-content:center;gap:52px;padding-top:58px;color:var(--white);text-align:center}
.stat{width:190px}
.stat b{display:block;font-size:50px;font-weight:700}
.stat b::after{content:"";display:block;width:70px;height:2px;background:var(--white);margin:10px auto}
.stat span{display:block;font-size:24px;font-weight:300;line-height:1.15}
.stat small{font-size:12px}

/* blog & news */
.sec-title{font-size:30px;font-weight:900;color:var(--orange)}
.post{position:absolute;top:3950px;width:185px}
.post-img{height:150px;background:linear-gradient(135deg,#6c6fa8,#c89a80)}
.post h4{color:var(--red);font-size:15px;font-weight:400;line-height:1.25;margin-top:12px}
.post small{display:block;font-size:10px;color:#555;margin-top:8px}
.news-item{position:absolute;left:789px;width:326px;display:flex;gap:14px}
.date{width:56px;height:56px;background:var(--blue);color:var(--white);text-align:center;font-weight:700;font-size:18px;line-height:1.05;padding-top:8px;flex:none}
.news-item p{font-size:15px;line-height:1.3;color:#333}

/* contact */
.contact{top:4288px;left:0;width:1200px;height:548px;background:linear-gradient(90deg,#8d8d8d 0%,#b9b9b9 45%,#e0e0e0 60%,#d4d4d4 100%)}
.contact-panel{position:absolute;left:89px;top:0;width:477px;height:548px;background:rgba(40,40,40,.55);padding:80px 40px 0}
.contact-panel h3{color:var(--white);font-size:22px;font-weight:900;margin-bottom:16px}
.field{background:var(--white);height:46px;font-size:13px;color:var(--muted);padding:14px 12px}
.row{display:flex;gap:10px;margin-bottom:12px}
.row .field{flex:1}
.field.big{height:84px;margin-bottom:12px}
.submit{background:var(--red);color:var(--white);text-align:center;font-size:22px;font-weight:700;padding:10px}
.info{color:var(--white);font-size:12px;margin-top:40px;line-height:2.6}
.info div{display:flex;gap:12px;align-items:center}
.pin{position:absolute}

/* footer */
.site-footer{top:4836px;left:0;width:1200px;height:307px;background:var(--blue);color:var(--white)}
.site-footer h5{font-size:18px;font-weight:900;margin-bottom:8px}
.site-footer ul{list-style:none;font-size:12px;line-height:1.7;columns:2;column-gap:20px}
.site-footer li::before{content:"› "}
.fb{position:absolute;left:925px;top:30px;width:190px;height:150px;background:var(--white);color:#333;font-size:12px;padding:10px}
.fb-thumb{width:40px;height:40px;background:#c9a58e;float:left;margin-right:8px}
.fb-like{display:inline-block;margin-top:6px;border:1px solid #ccc;padding:2px 8px;font-size:11px}
</style>
</head>
<body>

<header class="site-header">
  <div class="brand"><div class="brand-dot"></div><div class="brand-name">BRIGHT PATH<br>MENTORS</div></div>
  <div class="topbar">
    <div class="phone"><span class="phone-icon"><svg width="14" height="14" viewBox="0 0 24 24"><path fill="#fff" d="M6.6 10.8a15 15 0 0 0 6.6 6.6l2.2-2.2c.3-.3.7-.4 1-.2 1.1.4 2.3.6 3.6.6.6 0 1 .4 1 1V20c0 .6-.4 1-1 1A17 17 0 0 1 3 4c0-.6.4-1 1-1h3.5c.6 0 1 .4 1 1 0 1.3.2 2.5.6 3.6.1.3 0 .7-.2 1z"/></svg></span>1-800-555-0142</div>
    <div class="search"><span>Search location</span><b>GO</b></div>
  </div>
  <nav class="main-nav">
    <a class="active">HOME</a><a>ACADEMIC TUTORING</a><a>TEST PREP</a><a>PRICING</a><a>OUR TUTORS</a><a>ABOUT</a><a>CONTACT</a>
  </nav>
</header>

<section class="hero" role="img" aria-label="Photo of a young girl writing with a pencil at a desk">
  <div class="hero-copy">
    <div class="hero-kicker">ITS TIME TO</div>
    <div class="hero-title">START LEARNING</div>
    <div class="hero-rule"></div>
    <div class="hero-sub">Every child yearns to learn</div>
  </div>
</section>

<h2 class="abs intro-title">HOME TUTORING AT ITS BEST</h2>
<p class="abs intro-lead">quis nostrud exercitation ullamco laboris nisi ut aliquip ex ea commodo consequat</p>
<p class="abs intro-body">Sed ut perspiciatis unde omnis iste natus error sit voluptatem accusantium doloremque laudantium, totam rem aperiam, eaque ipsa quae ab illo inventore veritatis et quasi architecto beatae vitae dicta sunt explicabo. Nemo enim ipsam voluptatem quia voluptas sit aspernatur aut odit aut fugit, sed quia consequuntur magni dolores eos qui ratione voluptatem sequi nesciunt. Neque porro quisquam est, qui dolorem ipsum quia dolor sit amet, consectetur.</p>
<ul class="abs ticks">
  <li>Dolor sit amet, consectetur adipiscing elit sed do eiusmod</li>
  <li>Dolor sit amet, consectetur adipiscing elit</li>
  <li>Dolor sit amet, consectetur adipiscing elit</li>
  <li>Dolor sit amet, consectetur adipiscing elit</li>
</ul>
<div class="abs intro-photo" role="img" aria-label="Photo of a smiling girl in a classroom"></div>
<div class="abs quote-box">
  <span class="quote-mark">“</span>
  <p>Lorem ipsum dolor sit amet, consectetur adipiscing elit, sed do eiusmod tempor incididunt ut labore et dolore ma gnaquis nostrud exercitation ullamco labors</p>
  <div class="who">DANA WHITFIELD</div>
</div>

<section class="abs hex-band">
  <div class="hex" style="left:103px">
    <svg viewBox="0 0 310 292"><polygon points="78,0 232,0 310,146 232,292 78,292 0,146" fill="#f26a16"/></svg>
    <div class="hex-text">MAKING<br>STUDENTS LOVE<br>THEIR STUDIES</div><span class="hex-btn">VIEW REVIEWS</span>
  </div>
  <div class="hex" style="left:445px">
    <svg viewBox="0 0 310 292"><polygon points="78,0 232,0 310,146 232,292 78,292 0,146" fill="#f26a16"/></svg>
    <div class="hex-text">HIGHLY<br>PROFESSIONAL<br>TUTORING</div><span class="hex-btn">OUR WORK</span>
  </div>
  <div class="hex" style="left:787px">
    <svg viewBox="0 0 310 292"><polygon points="78,0 232,0 310,146 232,292 78,292 0,146" fill="#f26a16"/></svg>
    <div class="hex-text">HIGHEST<br>NUMBERS OF TOP<br>TUTORS</div><span class="hex-btn">FIND TUTOR</span>
  </div>
</section>

<h2 class="abs video-title">LOREM IPSUM DOLOR SIT AMET, CONSECTETUR</h2>
<div class="abs video-body">
  <p>Sed ut perspiciatis unde omnis iste natus error sit voluptatem accusantium doloremque laudantium, totam rem aperiam, eaque ipsa quae ab illo inventore veritatis et quasi architecto beatae vitae dicta sunt explicabo. Nemo enim ipsam voluptatem quia voluptas sit aspernatur aut odit aut fugit, sed quia consequuntur magni dolores eos qui ratione voluptatem sequi nesciunt magnam.</p>
  <p style="margin-top:16px"><span class="btn-orange">MORE VIDEOS</span></p>
</div>
<div class="abs badge"></div>
<div class="abs video" role="img" aria-label="Video still of a cartoon teacher reading with children"><div class="play"></div></div>

<section class="abs why">
  <h2>WHY BRIGHT PATH MENTORS?</h2>
  <div class="feature" style="left:89px;top:147px">
    <div class="feature-icon"><svg width="40" height="32" viewBox="0 0 40 32"><rect x="2" y="2" width="36" height="28" fill="none" stroke="#333" stroke-width="2.5"/><circle cx="13" cy="13" r="4" fill="#333"/><rect x="21" y="10" width="12" height="2.5" fill="#333"/><rect x="21" y="16" width="12" height="2.5" fill="#333"/><rect x="8" y="22" width="25" height="2.5" fill="#333"/></svg></div>
    <h3>Certified Tutors</h3><p>Sed ut perspiciatis unde omnis iste natus error sit voluptatem accusantium doloremque laudantium, totam rem aperiam, eaque ipsa quae ab illo inventore veritatis et quasi architecto beatae vitae dicta sunt explicabo.</p>
  </div>
  <div class="feature" style="left:617px;top:147px">
    <div class="feature-icon"><svg width="40" height="40" viewBox="0 0 40 40"><circle cx="20" cy="20" r="17" fill="none" stroke="#333" stroke-width="3"/><path d="M20 9v12l8 5" fill="none" stroke="#333" stroke-width="3"/></svg></div>
    <h3>Flexible Hours</h3><p>Sed ut perspiciatis unde omnis iste natus error sit voluptatem accusantium doloremque laudantium, totam rem aperiam, eaque ipsa quae ab illo inventore veritatis et quasi architecto beatae vitae dicta sunt explicabo.</p>
  </div>
  <div class="feature" style="left:89px;top:295px">
    <div class="feature-icon"><svg width="38" height="38" viewBox="0 0 38 38"><circle cx="19" cy="11" r="9" fill="#333"/><path d="M2 38c0-10 8-16 17-16s17 6 17 16z" fill="#333"/></svg></div>
    <h3>Personal Attention</h3><p>Sed ut perspiciatis unde omnis iste natus error sit voluptatem accusantium doloremque laudantium, totam rem aperiam, eaque ipsa quae ab illo inventore veritatis et quasi architecto beatae vitae dicta sunt explicabo.</p>
  </div>
  <div class="feature" style="left:617px;top:295px">
    <div class="feature-icon"><svg width="40" height="36" viewBox="0 0 40 36"><path d="M2 34 14 20l8 7L36 6" fill="none" stroke="#333" stroke-width="3.5"/><path d="M28 4h10v10" fill="none" stroke="#333" stroke-width="3.5"/></svg></div>
    <h3>Top Notch Results</h3><p>Sed ut perspiciatis unde omnis iste natus error sit voluptatem accusantium doloremque laudantium, totam rem aperiam, eaque ipsa quae ab illo inventore veritatis et quasi architecto beatae vitae dicta sunt explicabo.</p>
  </div>
  <div class="feature" style="left:353px;top:473px">
    <div class="feature-icon"><svg width="40" height="38" viewBox="0 0 40 38"><rect x="2" y="16" width="8" height="20" fill="#333"/><path d="M13 17 21 3c3 0 4 2 3 6l-2 6h12c3 0 4 3 3 5l-4 13c-1 2-2 3-4 3H13z" fill="#333"/></svg></div>
    <h3>Best Results Guaranteed</h3><p>Sed ut perspiciatis unde omnis iste natus error sit voluptatem accusantium doloremque laudantium, totam rem aperiam, eaque ipsa quae ab illo inventore veritatis et quasi architecto beatae vitae dicta sunt explicabo.</p>
  </div>
</section>

<section class="abs testi" role="img" aria-label="Darkened photo of an empty classroom behind a testimonial">
  <div class="testi-frame">Sed ut perspiciatis unde omnis iste natus error sit voluptatem accusantium doloremque laudantium, totam rem aperiam, eaque ipsa quae ab illo inventore veritatis et quasi architecto beatae vitae dicta sunt explicabo. Nemo enim ipsam voluptatem quia voluptas sit aspernatur aut odit aut fugit, sed quia consequuntur magni dolores eos qui ratione voluptatem sequi nesciunt.</div>
  <div class="avatar" role="img" aria-label="Portrait of the reviewer"></div>
  <div class="testi-name">Marcus Ellery</div>
  <div class="arrows">
    <svg width="18" height="24" viewBox="0 0 18 24"><path d="M14 2 4 12l10 10" fill="none" stroke="#f26a16" stroke-width="4"/></svg>
    <svg width="18" height="24" viewBox="0 0 18 24"><path d="m4 2 10 10L4 22" fill="none" stroke="#f26a16" stroke-width="4"/></svg>
  </div>
</section>

<section class="abs stats">
  <div class="stat"><b>3,596</b><span>CERTIFIED<br>CLIENTS</span><small>and counting</small></div>
  <div class="stat"><b>7,544</b><span>SUCCESSFULL<br>TESTS</span><small>and counting</small></div>
  <div class="stat"><b>349</b><span>POSITIONS<br>WON</span><small>and counting</small></div>
  <div class="stat"><b>58</b><span>SUBJECTS<br>COVERED</span><small>and counting</small></div>
</section>

<h2 class="abs sec-title" style="left:89px;top:3895px">OUR BLOG</h2>
<div class="post" style="left:89px"><div class="post-img" role="img" aria-label="Photo of a child at school"></div><h4>qui dolorem eum fugiat quo voluptas nulla pariatu</h4><small>July 14, 2016 by <b>Lena Ortiz</b></small></div>
<div class="post" style="left:316px"><div class="post-img" role="img" aria-label="Photo of a child at school"></div><h4>qui dolorem eum fugiat quo voluptas nulla pariatu</h4><small>July 14, 2016 by <b>Lena Ortiz</b></small></div>
<div class="post" style="left:539px"><div class="post-img" role="img" aria-label="Photo of a child at school"></div><h4>qui dolorem eum fugiat quo voluptas nulla pariatu</h4><small>July 14, 2016 by <b>Lena Ortiz</b></small></div>

<h2 class="abs sec-title" style="left:789px;top:3895px">NEWS</h2>
<div class="news-item" style="top:3950px"><div class="date">15<br>FEB</div><p>numquam eius modi tempora incidunt ut labore et dolore</p></div>
<div class="news-item" style="top:4025px"><div class="date">24<br>FEB</div><p>numquam eius modi tempora incidunt ut labore et dolore</p></div>
<div class="news-item" style="top:4100px"><div class="date">03<br>MAR</div><p>numquam eius modi tempora incidunt ut labore et dolore</p></div>
<div class="news-item" style="top:4175px"><div class="date">18<br>MAR</div><p>numquam eius modi tempora incidunt ut labore et dolore</p></div>

<section class="abs contact" role="img" aria-label="Grey street map of the service area">
  <svg class="pin" style="left:600px;top:30px" width="30" height="42" viewBox="0 0 30 42"><path d="M15 0C7 0 1 6 1 14c0 10 14 28 14 28s14-18 14-28C29 6 23 0 15 0z" fill="#444"/><circle cx="15" cy="14" r="5" fill="#ddd"/></svg>
  <svg class="pin" style="left:868px;top:188px" width="30" height="42" viewBox="0 0 30 42"><path d="M15 0C7 0 1 6 1 14c0 10 14 28 14 28s14-18 14-28C29 6 23 0 15 0z" fill="#444"/><circle cx="15" cy="14" r="5" fill="#ddd"/></svg>
  <svg class="pin" style="left:590px;top:385px" width="30" height="42" viewBox="0 0 30 42"><path d="M15 0C7 0 1 6 1 14c0 10 14 28 14 28s14-18 14-28C29 6 23 0 15 0z" fill="#444"/><circle cx="15" cy="14" r="5" fill="#ddd"/></svg>
  <div class="contact-panel">
    <h3>CONTACT US</h3>
    <div class="row"><div class="field">Name</div><div class="field">Email</div></div>
    <div class="field big">Message here...</div>
    <div class="submit">SUBMIT</div>
    <div class="info">
      <div><svg width="12" height="16" viewBox="0 0 12 16"><path d="M6 0a6 6 0 0 0-6 6c0 4 6 10 6 10s6-6 6-10a6 6 0 0 0-6-6z" fill="#fff"/></svg>120 Maple Row, Suite 200</div>
      <div><svg width="14" height="14" viewBox="0 0 24 24"><path fill="#fff" d="M6.6 10.8a15 15 0 0 0 6.6 6.6l2.2-2.2c.3-.3.7-.4 1-.2 1.1.4 2.3.6 3.6.6.6 0 1 .4 1 1V20c0 .6-.4 1-1 1A17 17 0 0 1 3 4c0-.6.4-1 1-1h3.5c.6 0 1 .4 1 1 0 1.3.2 2.5.6 3.6.1.3 0 .7-.2 1z"/></svg>1-800-555-0142</div>
      <div><svg width="14" height="11" viewBox="0 0 14 11"><rect width="14" height="11" fill="#fff"/><path d="m0 0 7 6 7-6" fill="none" stroke="#555"/></svg>hello@brightpathmentors.ca</div>
    </div>
  </div>
</section>

<footer class="abs site-footer">
  <div class="abs" style="left:89px;top:30px;width:230px">
    <h5>SUBJECTS</h5>
    <ul style="columns:1"><li>Elementary Tutoring</li><li>Foreign Languages</li><li>Elementary Tutoring</li><li>Foreign Languages</li></ul>
    <h5 style="margin-top:14px">LOCATIONS</h5>
    <ul><li>Toronto</li><li>Toronto</li><li>Toronto</li><li>Toronto</li><li>Toronto</li><li>Toronto</li></ul>
  </div>
  <div class="abs" style="left:345px;top:30px;width:280px">
    <h5>OTHER SUBJECTS</h5>
    <ul><li>Elementary Tutoring</li><li>Elementary Tutoring</li><li>Elementary Tutoring</li><li>Elementary Tutoring</li><li>Elementary Tutoring</li><li>Elementary Tutoring</li><li>Elementary Tutoring</li><li>Elementary Tutoring</li><li>Elementary Tutoring</li><li>Elementary Tutoring</li><li>Elementary Tutoring</li><li>Elementary Tutoring</li><li>Elementary Tutoring</li><li>Elementary Tutoring</li></ul>
  </div>
  <div class="abs" style="left:685px;top:30px;width:220px">
    <h5>COMPANY</h5>
    <ul style="columns:1"><li>Elementary Tutoring</li><li>Elementary Tutoring</li><li>Elementary Tutoring</li><li>Elementary Tutoring</li><li>Elementary Tutoring</li><li>Elementary Tutoring</li><li>Elementary Tutoring</li><li>Elementary Tutoring</li></ul>
  </div>
  <div class="fb">
    <div class="fb-thumb" role="img" aria-label="Page profile photo"></div>
    <b>Bright Path Mentors</b><br><span class="fb-like">Like Page</span>
    <p style="clear:both;margin-top:14px;font-size:11px">Be the first of your friends to like this</p>
  </div>
</footer>

</body>
</html>
```